Core Values poster for our office wall

We have a set of core values in our business and we want to create a nice looking poster to go up on our office wall.

Probably either A1 or A0 sizing.

It is important that the poster represents us as a company and our values.
You can get some ideas on us via the website colours/layout etc - www.marlowbrook.com.au

We need it to communicate our Values and how we love having a fun and encouraging environment.

Values: (which also spell out INSPIRED)
And some sub words related to that one

Initative - Ownership, accountability, innovation
Nurturing - Relationships, Community, Helpful
Success - Empowered
Passion - Fun, Relaxed
Integrity - Trust, Honesty, Respectful, Fortitude
Results - Knowledge, Confidence, Go-getter
Efficiency - Consistent, Organised, Fanatic Discipline
Dependability - Predictability, Security, Responsive, Execution

The below link contains some copies of our logo and also various ones of our company mascot.

https://marlowbrook.filequaybox.com/_layouts/15/guestaccess.aspx?folderid=4d21b8f07c3ea5d611b82af07e4813c9e&authkey=KqwTRmzo3pLdXc72yyHJ-Rk&e=9P2TdQ
Updates

Sorry everyone, A question made me realise I had left out the sub words to each of the main words. Here is an update. Initative - Ownership, accountability, innovation Nurturing - Relationships, Community, Helpful Success - Empowered Passion - Fun, Relaxed Integrity - Trust, Honesty, Respectful, Fortitude Results - Knowledge, Confidence, Go-getter Efficiency - Consistent, Organised, Fanatic Discipline Dependability - Predictability, Security, Responsive, Execution

Industry/Entity Type

Business

Requirements
Must have
• Good clean clear design
• Represent our company branding

```html
<!DOCTYPE html>
<html lang="en">
<head>
<meta charset="utf-8">
<title>Marlow Brook – Our Core Values</title>
<link rel="stylesheet" href="https://fonts.googleapis.com/css2?family=Arimo:wght@400;700&display=swap">
<style>
  :root {
    --paper: #ffffff;
    --ink: #000000;
    --panel: #000000;
    --title-accent: #5ec8ea;
    --brand: #2a78c8;
    --sky: #eef5fc;
    --grey-1: #e8e9eb;
    --grey-2: #e0e1e3;
    --grey-3: #d5d6d8;
    --grey-4: #cdcecf;
    --grey-5: #c5c6c8;
    --grey-6: #bcbdbf;
    --grey-7: #a9aaac;
    --grey-8: #939597;
  }
  html, body {
    margin: 0;
    padding: 0;
    width: 831px;
    height: 1200px;
    overflow: hidden;
    background: var(--paper);
  }
  .poster {
    display: block;
    width: 831px;
    height: 1200px;
  }
  .panel { fill: var(--panel); }
  .sky { fill: var(--sky); }
  .title {
    font-family: "Arimo", Arial, sans-serif;
    font-weight: 700;
    fill: var(--paper);
  }
  .title-accent { fill: var(--title-accent); }
  .brand-name {
    font-family: "Arimo", Arial, sans-serif;
    font-weight: 700;
    font-size: 25px;
    fill: var(--brand);
  }
  .value-name {
    font-family: "Arimo", Arial, sans-serif;
    font-weight: 700;
    font-size: 33px;
    fill: var(--paper);
  }
  .value-words {
    font-family: "Arimo", Arial, sans-serif;
    font-weight: 400;
    font-size: 22.5px;
    fill: var(--ink);
  }
  .row-1 { fill: var(--grey-1); }
  .row-2 { fill: var(--grey-2); }
  .row-3 { fill: var(--grey-3); }
  .row-4 { fill: var(--grey-4); }
  .row-5 { fill: var(--grey-5); }
  .row-6 { fill: var(--grey-6); }
  .row-7 { fill: var(--grey-7); }
  .row-8 { fill: var(--grey-8); }
</style>
</head>
<body>
<svg class="poster" viewBox="0 0 760 1100" preserveAspectRatio="none" xmlns="http://www.w3.org/2000/svg">
  <defs>
    <linearGradient id="band-initiative" x1="0" x2="1" y1="0" y2="0">
      <stop offset="0" stop-color="#2f6496"/><stop offset="0.55" stop-color="#244a6e"/><stop offset="1" stop-color="#0c1620"/>
    </linearGradient>
    <linearGradient id="band-success" x1="0" x2="1" y1="0" y2="0">
      <stop offset="0" stop-color="#6cc8e0"/><stop offset="0.55" stop-color="#3d7f92"/><stop offset="1" stop-color="#101c22"/>
    </linearGradient>
    <linearGradient id="band-integrity" x1="0" x2="1" y1="0" y2="0">
      <stop offset="0" stop-color="#5bbad6"/><stop offset="0.55" stop-color="#357488"/><stop offset="1" stop-color="#0f1a20"/>
    </linearGradient>
    <linearGradient id="band-efficiency" x1="0" x2="1" y1="0" y2="0">
      <stop offset="0" stop-color="#2a92d4"/><stop offset="0.55" stop-color="#1d5f8c"/><stop offset="1" stop-color="#0a1622"/>
    </linearGradient>
    <linearGradient id="chevron-nurturing" x1="0" x2="1" y1="0" y2="0">
      <stop offset="0" stop-color="#14202c"/><stop offset="0.5" stop-color="#1b4f78"/><stop offset="1" stop-color="#1f86c8"/>
    </linearGradient>
    <linearGradient id="chevron-passion" x1="0" x2="1" y1="0" y2="0">
      <stop offset="0" stop-color="#1a2a30"/><stop offset="0.5" stop-color="#3f8ea4"/><stop offset="1" stop-color="#6ad8f0"/>
    </linearGradient>
    <linearGradient id="chevron-results" x1="0" x2="1" y1="0" y2="0">
      <stop offset="0" stop-color="#1a2a30"/><stop offset="0.5" stop-color="#3f8ea4"/><stop offset="1" stop-color="#66d2ec"/>
    </linearGradient>
    <linearGradient id="chevron-dependability" x1="0" x2="1" y1="0" y2="0">
      <stop offset="0" stop-color="#121c26"/><stop offset="0.5" stop-color="#1f4a70"/><stop offset="1" stop-color="#3070aa"/>
    </linearGradient>
  </defs>

  <!-- frame -->
  <rect class="panel" x="18" y="18" width="724" height="1062"/>
  <polygon class="sky" points="570,18 742,18 742,246 373,246"/>

  <!-- header -->
  <text class="title" x="90" y="118"><tspan font-size="38">O</tspan><tspan font-size="30">UR</tspan></text>
  <text class="title" x="44" y="180"><tspan class="title-accent" font-size="60">C</tspan><tspan class="title-accent" font-size="46">ORE </tspan><tspan font-size="60">V</tspan><tspan font-size="46">ALUES</tspan></text>
  <circle cx="530" cy="152" r="7" fill="var(--brand)"/>
  <text class="brand-name" x="545" y="161">Marlow Brook</text>

  <!-- grey row backgrounds -->
  <polygon class="row-1" points="373,246 742,246 742,348 285,348"/>
  <rect class="row-2" x="285" y="350" width="457" height="103"/>
  <polygon class="row-3" points="373,455 742,455 742,557 285,557"/>
  <rect class="row-4" x="285" y="559" width="457" height="103"/>
  <polygon class="row-5" points="373,664 742,664 742,766 285,766"/>
  <rect class="row-6" x="285" y="768" width="457" height="102"/>
  <polygon class="row-7" points="373,872 742,872 742,974 285,974"/>
  <rect class="row-8" x="285" y="976" width="457" height="102"/>

  <!-- value bands -->
  <polygon fill="url(#band-initiative)" points="18,246 375,246 285,348 18,348"/>
  <polygon fill="url(#chevron-nurturing)" points="65,350 490,350 525,401 490,453 112,453"/>
  <polygon fill="url(#band-success)" points="18,455 375,455 285,557 18,557"/>
  <polygon fill="url(#chevron-passion)" points="65,559 490,559 525,610 490,662 112,662"/>
  <polygon fill="url(#band-integrity)" points="18,664 375,664 285,766 18,766"/>
  <polygon fill="url(#chevron-results)" points="65,768 490,768 525,819 490,870 112,870"/>
  <polygon fill="url(#band-efficiency)" points="18,872 375,872 285,974 18,974"/>
  <polygon fill="url(#chevron-dependability)" points="65,976 440,976 475,1027 440,1078 112,1078"/>

  <!-- value names -->
  <text class="value-name" x="52" y="312">INITIATIVE</text>
  <text class="value-name" x="168" y="413">NURTURING</text>
  <text class="value-name" x="52" y="514">SUCCESS</text>
  <text class="value-name" x="168" y="621">PASSION</text>
  <text class="value-name" x="52" y="727">INTEGRITY</text>
  <text class="value-name" x="168" y="832">REULTS</text>
  <text class="value-name" x="52" y="935">EFFICIENCY</text>
  <text class="value-name" x="138" y="1037">DEPENDABILITY</text>

  <!-- supporting words -->
  <text class="value-words" x="384" y="278">Ownership</text>
  <text class="value-words" x="353" y="309">Accountability</text>
  <text class="value-words" x="316" y="342">Innovation</text>

  <text class="value-words" x="540" y="380">Relationships</text>
  <text class="value-words" x="563" y="412">Community</text>
  <text class="value-words" x="547" y="444">Helpful</text>

  <text class="value-words" x="346" y="518">Empowered</text>

  <text class="value-words" x="520" y="610">Fun</text>
  <text class="value-words" x="506" y="642">Relaxed</text>

  <text class="value-words" x="371" y="709">Trust , Honesty</text>
  <text class="value-words" x="333" y="741">Respectful , Fortitude</text>

  <text class="value-words" x="521" y="801">Knowledge</text>
  <text class="value-words" x="551" y="833">Confidence</text>
  <text class="value-words" x="537" y="865">Go - getter</text>

  <text class="value-words" x="384" y="899">Consistent</text>
  <text class="value-words" x="353" y="931">Organised</text>
  <text class="value-words" x="324" y="963">Fanatic Discipline</text>

  <text class="value-words" x="486" y="1003">Predictability</text>
  <text class="value-words" x="471" y="1035">Security , Responsive</text>
  <text class="value-words" x="486" y="1067">Execution</text>
</svg>
</body>
</html>
```